Structural Engineering Business Card

Veltrow Drafts does residential house plans for clients in Central Florida. Would like simple but elegant business card that is appropriate for a house plan engineering company. Prefer black business card with black/white them but open to other shades of blue. I uploaded a sample card that I came across that looked good but please come up with your own creative designs.

Contact Information for Business Card

Name, Title, Phone, Email, Address, website

```html
<!DOCTYPE html>
<html lang="en">
<head>
<meta charset="utf-8">
<title>Veltrow Drafts — Business Card</title>
<link href="https://fonts.googleapis.com/css2?family=Lato:wght@400;700;900&display=swap" rel="stylesheet">
<style>
  :root {
    --page-bg-center: #3b3b3b;
    --page-bg-edge: #161616;
    --card-top: #2f2f2f;
    --card-bottom: #232323;
    --card-edge: #111111;
    --ink: #f2f2f2;
    --ink-soft: #bdbdbd;
    --ink-muted: #8c8c8c;
    --rule: #d9d9d9;
    --emboss: #3a3a3a;
    --emboss-shine: #9a9a9a;
  }
  * { box-sizing: border-box; margin: 0; padding: 0; }
  html, body {
    width: 1200px; height: 900px; overflow: hidden;
  }
  body {
    background: radial-gradient(ellipse at 50% 45%, var(--page-bg-center), var(--page-bg-edge) 75%);
    font-family: "Lato", sans-serif;
    color: var(--ink);
    position: relative;
  }
  .card {
    position: absolute;
    left: 340px;
    width: 520px;
    height: 300px;
    border-radius: 22px;
    background: linear-gradient(160deg, var(--card-top), var(--card-bottom));
    box-shadow: 0 2px 0 var(--card-edge), 0 5px 0 #1b1b1b, 0 8px 0 var(--card-edge), 0 26px 40px rgba(0,0,0,.55);
  }
  .card--front { top: 110px; }
  .card--back  { top: 490px; }

  /* Front */
  .contact-block {
    position: absolute;
    left: 38px; top: 36px;
  }
  .person-name {
    font-weight: 700;
    font-size: 20px;
    letter-spacing: .5px;
    text-transform: uppercase;
  }
  .person-title {
    font-size: 11px;
    letter-spacing: 1.5px;
    color: var(--ink-soft);
    text-transform: uppercase;
    margin-top: 3px;
    margin-bottom: 14px;
  }
  .contact-line {
    display: flex; align-items: center; gap: 8px;
    font-size: 13.5px;
    color: var(--ink-soft);
    line-height: 21px;
  }
  .contact-line svg { width: 10px; height: 10px; flex: none; }
  .divider {
    position: absolute;
    left: 38px; top: 178px;
    width: 390px; height: 1px;
    background: var(--rule);
  }
  .brand-mark {
    position: absolute;
    right: 38px; top: 38px;
    display: flex; align-items: center; gap: 10px;
    font-weight: 900;
    font-size: 26px;
    letter-spacing: .3px;
    color: var(--ink);
    text-transform: uppercase;
  }
  .brand-mark .brand-square {
    width: 14px; height: 14px; background: var(--ink);
  }
  .address {
    position: absolute;
    right: 40px; bottom: 34px;
    font-size: 15px;
    line-height: 21px;
    color: var(--ink);
    text-align: left;
  }

  /* Back */
  .back-brand {
    position: absolute;
    inset: 0;
    display: flex; align-items: center; justify-content: center;
    font-weight: 900;
    font-size: 46px;
    letter-spacing: .5px;
    text-transform: uppercase;
    color: var(--emboss-shine);
    opacity: .55;
  }
</style>
</head>
<body>

  <section class="card card--front" aria-label="Card front">
    <div class="contact-block">
      <p class="person-name">Daniel Harrow</p>
      <p class="person-title">Director</p>
      <p class="contact-line">
        <svg viewBox="0 0 10 10" aria-hidden="true"><path d="M2 0.8 L3.6 2.8 L2.7 3.8 Q3.8 6.2 6.2 7.3 L7.2 6.4 L9.2 8 L8 9.4 Q3 8.6 0.6 2 Z" fill="currentColor"/></svg>
        407.555.0183
      </p>
      <p class="contact-line">
        <svg viewBox="0 0 10 10" aria-hidden="true"><rect x="0.7" y="2" width="8.6" height="6" fill="none" stroke="currentColor" stroke-width="1"/><path d="M0.7 2 L5 5.5 L9.3 2" fill="none" stroke="currentColor" stroke-width="1"/></svg>
        info@VeltrowDrafts.com
      </p>
      <p class="contact-line">
        <svg viewBox="0 0 10 10" aria-hidden="true"><circle cx="5" cy="5" r="4.2" fill="none" stroke="currentColor" stroke-width="1"/><ellipse cx="5" cy="5" rx="1.8" ry="4.2" fill="none" stroke="currentColor" stroke-width=".8"/><path d="M0.8 5 H9.2" stroke="currentColor" stroke-width=".8"/></svg>
        www.VeltrowDrafts.com
      </p>
    </div>

    <div class="brand-mark">
      <span class="brand-square" aria-hidden="true"></span>
      <span>Veltrow Drafts</span>
    </div>

    <div class="divider" aria-hidden="true"></div>

    <address class="address" style="font-style:normal">
      1148 Corlan Avenue<br>
      Ocala, FL 34471
    </address>
  </section>

  <section class="card card--back" aria-label="Card back">
    <div class="back-brand">Veltrow Drafts</div>
  </section>

</body>
</html>
```